Copperleaf Motorized Shade Business Card

Hello, we've had our logo made. Now we are looking for a clean and cool looking business card. One side can just be the logo with any design elements that might look good with it. The other side will be Name, Phone Number and Email. There will not be an address on the card.

```html
<!DOCTYPE html>
<html lang="en">
<head>
<meta charset="utf-8">
<title>Copperleaf Motorized Shade – Business Card</title>
<link href="https://fonts.googleapis.com/css2?family=Open+Sans:wght@400;600;700;800&display=swap" rel="stylesheet">
<style>
  :root{
    --stage:#404248;
    --card-glow:#1ab0ea;
    --card-mid:#0b86cc;
    --card-edge:#064a94;
    --brand-navy:#0c3d82;
    --accent-yellow:#f6b90c;
    --text-white:#ffffff;
    --divider:rgba(120,210,255,.45);
  }
  *{margin:0;padding:0;box-sizing:border-box}
  html,body{width:1200px;height:840px;overflow:hidden}
  body{
    background:var(--stage);
    font-family:"Open Sans",Arial,sans-serif;
    position:relative;
  }
  .card{
    position:absolute;
    width:500px;height:286px;
    top:277px;
    border-radius:3px;
    overflow:hidden;
    background:radial-gradient(ellipse at 50% 45%,var(--card-glow) 0%,var(--card-mid) 45%,var(--card-edge) 100%);
    box-shadow:0 18px 40px rgba(0,0,0,.45);
  }
  .card--front{left:70px}
  .card--back{left:630px}

  .brand{
    position:absolute;
    display:flex;align-items:center;gap:10px;
    color:var(--brand-navy);
    font-weight:800;
    text-transform:uppercase;
  }
  .brand__mark{width:16px;height:16px;background:var(--accent-yellow);flex:none}
  .brand__name{font-size:26px;letter-spacing:1px;line-height:1}
  .brand__tagline{
    display:block;font-size:9px;letter-spacing:4px;font-weight:800;margin-top:4px;
  }

  .card--front .brand{left:38px;top:112px}
  .divider{
    position:absolute;left:258px;top:60px;width:1px;height:166px;
    background:var(--divider);
  }
  .contact{
    position:absolute;left:286px;top:96px;color:var(--text-white);
  }
  .contact__name{color:var(--accent-yellow);font-weight:700;font-size:22px;line-height:1.1;letter-spacing:.5px}
  .contact__role{font-size:12px;font-weight:600;margin-bottom:16px}
  .contact__row{display:flex;align-items:center;gap:8px;font-size:14px;font-weight:600;margin-top:4px}
  .contact__row svg{width:12px;height:12px;flex:none}

  .card--back .brand{left:50%;top:50%;transform:translate(-50%,-62%)}
  .card--back .brand__name{font-size:32px}
  .watermark{
    position:absolute;left:300px;top:200px;
    color:var(--brand-navy);opacity:.35;
    font-weight:800;font-size:70px;line-height:1;white-space:nowrap;text-transform:uppercase;
  }
</style>
</head>
<body>

<section class="card card--front" aria-label="Business card front">
  <div class="brand">
    <span class="brand__mark"></span>
    <span><span class="brand__name">Copperleaf</span><span class="brand__tagline">Motorized Shade</span></span>
  </div>
  <div class="divider"></div>
  <div class="contact">
    <p class="contact__name">NAME</p>
    <p class="contact__role">Designation</p>
    <p class="contact__row">
      <svg viewBox="0 0 24 24" aria-hidden="true"><path fill="#f6b90c" d="M6.6 10.8a15.1 15.1 0 0 0 6.6 6.6l2.2-2.2c.3-.3.7-.4 1-.2 1.1.4 2.3.6 3.6.6.6 0 1 .4 1 1V20c0 .6-.4 1-1 1A17 17 0 0 1 3 4c0-.6.4-1 1-1h3.5c.6 0 1 .4 1 1 0 1.3.2 2.5.6 3.6.1.3 0 .7-.2 1z"/></svg>
      Phone Number
    </p>
    <p class="contact__row">
      <svg viewBox="0 0 24 24" aria-hidden="true"><rect x="2" y="5" width="20" height="14" rx="2" fill="#f6b90c"/><path d="M3 6l9 7 9-7" fill="none" stroke="#0b86cc" stroke-width="2"/></svg>
      Email ID
    </p>
  </div>
</section>

<section class="card card--back" aria-label="Business card back">
  <div class="watermark" aria-hidden="true">Copperleaf</div>
  <div class="brand">
    <span class="brand__mark"></span>
    <span><span class="brand__name">Copperleaf</span><span class="brand__tagline">Motorized Shade</span></span>
  </div>
</section>

</body>
</html>
```